Business Card for a Wedding Films Business

We require a business card design for our business 'Lewis Marrow Wedding Films'. The logo needs to look classy and high end.

Target Market(s)

Wedding Couples

Contact Information for Business Card

Lewis Marrow Wedding Films
07312 605 227
films@lewismarrowreels.com
www.lewismarrowreels.com

Circlo: @lewismarrowweddingfilms
Lumio: @lewismarrowfilms

Font styles to use
Sans Serif

Requirements
Must have
• Social media icons - Circlo and Lumio

```html
<!DOCTYPE html>
<html lang="en">
<head>
<meta charset="utf-8">
<title>Lewis Marrow Wedding Films – Business Card</title>
<link rel="stylesheet" href="https://fonts.googleapis.com/css2?family=Jost:wght@500&family=Source+Sans+3:wght@400&display=swap">
<style>
  :root {
    --backdrop: #f3f2ee;
    --cream: #ddd5c4;
    --tan: #b5927a;
    --ink-light: #f4f0e7;
    --crop: #6e6e6e;
  }
  html, body {
    margin: 0;
    padding: 0;
    overflow: hidden;
  }
  body {
    width: 1115px;
    height: 1200px;
    background: var(--backdrop);
    position: relative;
  }
  .card {
    position: absolute;
    width: 689px;
    height: 414px;
    box-shadow: 14px 18px 22px rgba(0, 0, 0, 0.22);
  }
  .card svg { display: block; }
  .card--front { left: 208px; top: 140px; background: var(--cream); }
  .card--back  { left: 206px; top: 637px; background: var(--tan); }
  .brand-name {
    font-family: "Jost", sans-serif;
    font-weight: 500;
  }
  .network-name {
    font-family: "Jost", sans-serif;
    font-weight: 500;
    font-size: 9px;
    letter-spacing: 0.5px;
    fill: var(--tan);
  }
  .contact-text {
    font-family: "Source Sans 3", sans-serif;
    font-weight: 400;
    font-size: 16px;
    fill: var(--ink-light);
  }
  .crop-mark { stroke: var(--crop); stroke-width: 0.8; fill: none; }
</style>
</head>
<body>

<div class="card card--front">
  <svg width="689" height="414" viewBox="0 0 689 414">
    <path class="crop-mark" d="M26 0V26H0 M663 0V26H689 M26 414V388H0 M663 414V388H689"/>
    <line x1="0" y1="213" x2="219" y2="213" stroke="var(--tan)" stroke-width="2.5"/>
    <line x1="468" y1="213" x2="689" y2="213" stroke="var(--tan)" stroke-width="2.5"/>
    <circle cx="344" cy="176" r="32" fill="none" stroke="var(--tan)" stroke-width="3"/>
    <text class="brand-name" x="212" y="254" font-size="29" fill="var(--tan)" textLength="266" lengthAdjust="spacing">LEWIS MARROW</text>
    <text class="brand-name" x="253" y="285" font-size="14" fill="var(--tan)" textLength="185" lengthAdjust="spacing">WEDDING FILMS</text>
  </svg>
</div>

<div class="card card--back">
  <svg width="689" height="414" viewBox="0 0 689 414">
    <path class="crop-mark" d="M26 0V26H0 M663 0V26H689 M26 414V388H0 M663 414V388H689"/>

    <circle cx="192" cy="188" r="27" fill="none" stroke="var(--cream)" stroke-width="3"/>
    <text class="brand-name" x="93" y="246" font-size="21" fill="var(--cream)" textLength="194" lengthAdjust="spacing">LEWIS MARROW</text>
    <text class="brand-name" x="125" y="270" font-size="10" fill="var(--cream)" textLength="134" lengthAdjust="spacing">WEDDING FILMS</text>

    <rect class="contact-spine" x="367.5" y="0" width="5" height="414" fill="var(--cream)"/>

    <g class="contact-icon contact-icon--phone">
      <circle cx="370" cy="81" r="21" fill="var(--cream)"/>
      <path d="M361 70c2-1 4 0 5 2l2 4c0 2-1 3-2 3 1 3 3 5 6 6 0-1 1-2 3-2l4 2c2 1 3 3 2 5-2 3-5 3-8 2-6-3-10-7-13-13-1-3-1-7 1-9z" fill="var(--tan)"/>
    </g>
    <g class="contact-icon contact-icon--mail">
      <circle cx="370" cy="147" r="21" fill="var(--cream)"/>
      <rect x="357" y="139" width="26" height="17" rx="1.5" fill="var(--tan)"/>
      <path d="M358 140l12 9 12-9 M358 155l9-7 M382 155l-9-7" stroke="var(--cream)" stroke-width="0.9" fill="none"/>
    </g>
    <g class="contact-icon contact-icon--web" fill="none" stroke="var(--tan)" stroke-width="1.3">
      <circle cx="370" cy="212" r="21" fill="var(--cream)" stroke="none"/>
      <circle cx="370" cy="212" r="13"/>
      <ellipse cx="370" cy="212" rx="6" ry="13"/>
      <path d="M370 199v26 M357 212h26 M359 205h22 M359 219h22"/>
    </g>
    <g class="contact-icon contact-icon--social">
      <circle cx="370" cy="278" r="21" fill="var(--cream)"/>
      <text class="network-name" x="370" y="281" text-anchor="middle">LUMIO</text>
    </g>
    <g class="contact-icon contact-icon--social">
      <circle cx="370" cy="341" r="21" fill="var(--cream)"/>
      <text class="network-name" x="370" y="344" text-anchor="middle">CIRCLO</text>
    </g>

    <text class="contact-text" x="422" y="87">07312 605 227</text>
    <text class="contact-text" x="421" y="153">films@lewismarrowreels.com</text>
    <text class="contact-text" x="422" y="218">www.lewismarrowreels.com</text>
    <text class="contact-text" x="421" y="283">@lewismarrowfilms</text>
    <text class="contact-text" x="422" y="346">@lewismarrowweddingfilms</text>
  </svg>
</div>

</body>
</html>
```